Storm Restoration Contractor needs a professional letterhead design

Looking for a professional letterhead design. Not looking for your cheapo MS Word standard ones that are readily available. Dont want it to be cookie cutter look like ones readily available online. We just recently changed our logo and want to freshen up all our documents. Our company handles restoring a property back to a pre-loss condition after a storm damages it. For example, wind, hail, flood, fire losses.

Target Market(s)

Property Owners, Homeowners, Property Owners, Commercial Property Owners, Property Management Companies

Industry/Entity Type

Construction Company

Requirements
Must have
• Professional, Use 1 of 2 logo options
• Storm Restoration, Roofing, Siding, Windows

```html
<!DOCTYPE html>
<html lang="en">
<head>
<meta charset="utf-8">
<title>Stormline Exteriors Letterhead</title>
<link href="https://fonts.googleapis.com/css2?family=Arimo:wght@400;700&display=swap" rel="stylesheet">
<style>
  :root {
    --backdrop: #eceded;
    --paper: #ffffff;
    --brand-blue: #2a78c8;
    --brand-grey: #4a4d52;
    --ink: #3a3a3a;
    --soft-lavender: #e4e8f5;
    --muted: #555;
  }
  html, body {
    margin: 0;
    padding: 0;
    width: 1200px;
    height: 795px;
    overflow: hidden;
    background: var(--backdrop);
    font-family: "Arimo", Arial, sans-serif;
  }
  .letterhead {
    position: absolute;
    left: 331px;
    top: 17px;
    width: 538px;
    height: 760px;
    background: var(--paper);
    box-shadow: 0 2px 10px rgba(0,0,0,0.12);
    overflow: hidden;
  }
  .decor {
    position: absolute;
    inset: 0;
    width: 538px;
    height: 760px;
  }
  .brand {
    position: absolute;
    left: 38px;
    top: 58px;
    display: flex;
    align-items: center;
    gap: 8px;
  }
  .brand-dot {
    width: 26px;
    height: 26px;
    border-radius: 50%;
    background: var(--brand-blue);
  }
  .brand-name {
    font-weight: 700;
    font-size: 13px;
    letter-spacing: 1.5px;
    text-transform: uppercase;
    color: var(--brand-blue);
  }
  .contact {
    position: absolute;
    right: 32px;
    top: 34px;
    text-align: right;
    font-size: 7.5px;
    line-height: 11px;
    color: var(--muted);
  }
  .contact-line {
    display: flex;
    justify-content: flex-end;
    align-items: center;
    gap: 4px;
  }
  .contact-icon {
    width: 8px;
    height: 8px;
  }
  .letter {
    position: absolute;
    left: 40px;
    top: 250px;
    width: 450px;
    font-size: 10.5px;
    line-height: 14.5px;
    color: var(--ink);
  }
  .salutation {
    font-weight: 700;
    font-size: 11.5px;
    margin: 0 0 6px;
  }
  .letter p {
    margin: 0 0 12px;
  }
  .signature {
    position: absolute;
    left: 42px;
    top: 520px;
    width: 90px;
    height: 32px;
    background: linear-gradient(90deg, #f2f2f2, #e6e6e6);
    border-radius: 3px;
  }
</style>
</head>
<body>
  <main class="letterhead">
    <svg class="decor" viewBox="0 0 538 760" aria-hidden="true">
      <path class="lavender-arc" d="M0,300 C120,285 205,165 222,0 L252,0 C238,185 140,318 0,334 Z" fill="var(--soft-lavender)"/>
      <path class="corner-band-grey" d="M538,548 C455,575 398,660 388,760 L400,760 C412,668 465,596 538,572 Z" fill="var(--brand-grey)"/>
      <path class="corner-band-blue" d="M538,574 C468,598 416,668 404,760 L538,760 Z" fill="var(--brand-blue)"/>
      <text class="corner-url" x="0" y="0" transform="translate(450,742) rotate(-52)" font-family="Arimo, Arial, sans-serif" font-size="9.5" letter-spacing="1" fill="#ffffff">www.stormlineexteriors.com</text>
    </svg>

    <div class="brand">
      <span class="brand-dot"></span>
      <span class="brand-name">Stormline Exteriors</span>
    </div>

    <address class="contact" style="font-style: normal;">
      <div class="contact-line">2750 Harbor Ridge Rd</div>
      <div class="contact-line">Fairview, CA 95600</div>
      <div class="contact-line">(555) 204-7731
        <svg class="contact-icon" viewBox="0 0 10 10"><circle cx="5" cy="5" r="5" fill="var(--brand-blue)"/><path d="M3,2.5 L4.2,2.5 L4.6,4 L3.9,4.5 C4.3,5.4 4.8,5.9 5.6,6.2 L6.1,5.5 L7.5,5.9 L7.5,7.1 C5,7.3 2.8,5 3,2.5 Z" fill="#fff"/></svg>
      </div>
      <div class="contact-line">(555) 204-7732
        <svg class="contact-icon" viewBox="0 0 10 10"><circle cx="5" cy="5" r="5" fill="var(--brand-blue)"/><rect x="3" y="3.5" width="4" height="3" fill="#fff"/></svg>
      </div>
      <div class="contact-line">hello@stormlineexteriors.com
        <svg class="contact-icon" viewBox="0 0 10 10"><circle cx="5" cy="5" r="5" fill="var(--brand-blue)"/><path d="M2.8,3.3 H7.2 V6.7 H2.8 Z M2.8,3.3 L5,5.2 L7.2,3.3" fill="none" stroke="#fff" stroke-width="0.7"/></svg>
      </div>
    </address>

    <section class="letter">
      <p class="salutation">Dear Mr. Carter,</p>
      <p>Lorem Ipsum is simply dummy text of the printing and typesetting industry. Lorem Ipsum has been the industry's standard dummy text ever since the 1500s, when an unknown printer took a galley of type and scrambled it to make a type specimen book. It has survived not only five centuries, but also the leap into electronic typesetting, remaining essentially unchanged.</p>
      <p>The standard chunk of Lorem Ipsum used since the 1500s is reproduced below for those interested. Sections 1.10.32 and 1.10.33 from "de Finibus Bonorum et Malorum" by Cicero are also reproduced in their exact original form, accompanied by English versions from the 1914 translation by H. Rackham.</p>
      <p>Lorem Ipsum is simply dummy text of the printing and typesetting industry. Lorem Ipsum has been the industry's standard dummy text ever since the 1500s, when an unknown printer took a galley of type and scrambled it to make a type specimen book. It has survived not only five centuries, but also the leap into electronic typesetting, remaining essentially unchanged. It was popularised in the</p>
    </section>

    <div class="signature" role="img" aria-label="Handwritten signature of the sender"></div>
  </main>
</body>
</html>
```